TM Holdings-Homes for Tomorrow's World

TM Holdings is a Residential Real Estate company which specializes in buying and selling homes. We pride ourselves on service, expertise, and building relationships. I would like to do a Billboard Ad for a The Size is 14 feet (Height) x 48 feet (width) displaying our current motto for "Real Estate of the Future" We have launched new programs and working with leaders in our industy Pavrit and other tech companies and changing the way Real Estate is done in Las Vegas, NV. Its exciting and NEW so we want to get the word out. Color Scheme Red, White, Grey and maybe black. Logo is uploaded and so is a picture head shot. I would like to see options with my headshot and with out.

```html
<!DOCTYPE html>
<html lang="en">
<head>
<meta charset="utf-8">
<title>TM Holdings – Billboard</title>
<link rel="stylesheet" href="https://fonts.googleapis.com/css2?family=Marcellus&display=swap">
<style>
  :root {
    --brand-red: #c0202a;
    --charcoal: #2e2e30;
    --silver: #b9b9bd;
    --white: #ffffff;
    --ink: #111111;
    --backdrop: #e9e7e7;
    --scene-light: #b8adb4;
    --scene-mid: #7d7280;
    --scene-dark: #3d4a3a;
    --suit: #1d2433;
  }
  * { margin: 0; padding: 0; box-sizing: border-box; }
  html, body {
    width: 1200px; height: 743px; overflow: hidden;
    background: var(--backdrop);
    font-family: "Marcellus", serif;
  }
  .billboard {
    position: absolute; left: 40px; top: 208px;
    width: 1120px; height: 327px; overflow: hidden;
    background: var(--white);
    box-shadow: 0 14px 24px rgba(0,0,0,0.18);
  }
  .house-scene {
    position: absolute; inset: 0;
    background:
      radial-gradient(ellipse at 92% 10%, var(--scene-dark) 0%, transparent 45%),
      linear-gradient(180deg, #8a8190 0%, var(--scene-light) 45%, var(--scene-mid) 100%);
  }
  .white-fade {
    position: absolute; inset: 0;
    background: linear-gradient(90deg, var(--white) 0%, var(--white) 36%, rgba(255,255,255,0.55) 48%, rgba(255,255,255,0) 62%);
  }
  .swooshes { position: absolute; inset: 0; width: 1120px; height: 327px; }
  .headshot {
    position: absolute; left: 488px; top: 28px; width: 300px; height: 299px;
    border-radius: 130px 130px 0 0;
    background: linear-gradient(180deg, #5a4638 0%, #c9a08a 22%, #c49a86 45%, var(--suit) 62%, var(--suit) 100%);
  }
  .brand {
    position: absolute; left: 55px; top: 140px; width: 400px;
    text-align: center;
  }
  .brand-name {
    font-size: 54px; line-height: 1; color: var(--brand-red);
    letter-spacing: 1px;
  }
  .tagline {
    position: absolute; left: 55px; top: 225px; width: 400px;
    text-align: center; text-transform: uppercase;
  }
  .tagline-lead { font-size: 38px; line-height: 1.1; color: var(--brand-red); }
  .tagline-tail { font-size: 28px; line-height: 1.3; color: var(--ink); }
  .pitch {
    position: absolute; right: 35px; top: 48px;
    text-align: right; color: var(--white); text-transform: uppercase;
  }
  .pitch-intro { font-size: 28px; line-height: 1.1; }
  .pitch-highlight {
    display: inline-block; margin-top: 6px;
    background: var(--brand-red); padding: 2px 10px 0;
    font-size: 38px; line-height: 1.15;
  }
  .pitch-detail { font-size: 22px; line-height: 1.25; margin-top: 4px; }
  .pitch-phone { font-size: 38px; line-height: 1.3; margin-top: 6px; letter-spacing: 1px; }
</style>
</head>
<body>
  <div class="billboard">
    <div class="house-scene" role="img" aria-label="Softly blurred photo of a suburban house with trees"></div>
    <div class="white-fade"></div>

    <svg class="swooshes" viewBox="0 0 1120 327" aria-hidden="true">
      <path d="M0,14 C90,66 230,92 340,92 C460,92 560,48 650,0" fill="none" stroke="var(--silver)" stroke-width="12"/>
      <path d="M0,8 C90,60 230,86 340,86 C460,86 560,42 640,0" fill="none" stroke="var(--charcoal)" stroke-width="9"/>
      <path d="M0,0 H610 C530,46 420,72 300,72 C170,72 70,46 0,14 Z" fill="var(--brand-red)"/>
      <path d="M580,327 C700,280 860,258 980,270 C1050,277 1095,295 1120,312" fill="none" stroke="var(--white)" stroke-width="7"/>
      <path d="M640,327 C740,292 880,278 990,288 C1050,294 1095,308 1120,320 V327 Z" fill="var(--brand-red)"/>
    </svg>

    <div class="headshot" role="img" aria-label="Headshot of the agent in a dark blazer and blue shirt"></div>

    <div class="brand">
      <div class="brand-name">TM HOLDINGS</div>
    </div>

    <div class="tagline">
      <div class="tagline-lead">Homes for</div>
      <div class="tagline-tail">Tomorrow's World</div>
    </div>

    <div class="pitch">
      <div class="pitch-intro">We pride ourselves</div>
      <div class="pitch-highlight">On service</div>
      <div class="pitch-detail">Expertise &amp; building<br>relationships</div>
      <div class="pitch-phone">702-555-0148</div>
    </div>
  </div>
</body>
</html>
```